Book Cover Design

Design with title UNWAVERING
Subtitle: Ways to Kindle the Spark of Resolve
Author Name: Carla Jean Morrow
Put DAILY MERIDIAN BESTSELLER at top
Shimmer design, see inspirational images attached

```html
<!DOCTYPE html>
<html lang="en">
<head>
<meta charset="utf-8">
<title>Unwavering — Book Cover</title>
<link rel="stylesheet" href="https://fonts.googleapis.com/css2?family=Montserrat:wght@600;700&family=Anton&family=Source+Sans+3:wght@700&display=swap">
<style>
  :root {
    --page-bg: #ffffff;
    --ink: #111111;
    --magenta: #ee4ee8;
    --magenta-soft: #f58ff0;
    --blush: #fbe6f3;
    --violet: #a25cf0;
    --glow: #ffffff;
  }
  * { margin: 0; padding: 0; box-sizing: border-box; }
  html, body {
    width: 1200px;
    height: 825px;
    overflow: hidden;
    background: var(--page-bg);
  }
  .canvas {
    position: relative;
    width: 1200px;
    height: 825px;
  }
  .book-cover {
    position: absolute;
    left: 346px;
    top: 32px;
    width: 508px;
    height: 760px;
    overflow: hidden;
    background:
      radial-gradient(circle at 40% 34%, rgba(255,255,255,0.95) 0, rgba(255,255,255,0.55) 4%, rgba(255,255,255,0) 14%),
      radial-gradient(ellipse 40% 55% at 88% 38%, rgba(251,230,243,0.95) 0, rgba(251,230,243,0) 70%),
      radial-gradient(ellipse 45% 30% at 60% 14%, rgba(255,255,255,0.7) 0, rgba(255,255,255,0) 70%),
      radial-gradient(ellipse 60% 30% at 70% 58%, rgba(255,240,248,0.85) 0, rgba(255,240,248,0) 75%),
      radial-gradient(ellipse 55% 45% at 0% 100%, var(--violet) 0, rgba(162,92,240,0) 70%),
      radial-gradient(ellipse 70% 40% at 50% 88%, var(--magenta) 0, rgba(238,78,232,0) 80%),
      linear-gradient(160deg, var(--magenta-soft) 0%, var(--blush) 45%, var(--magenta) 100%);
  }
  .book-cover__shimmer {
    position: absolute;
    inset: 0;
    background:
      radial-gradient(circle at 55% 78%, rgba(255,255,255,0.25) 0, rgba(255,255,255,0) 10%),
      radial-gradient(circle at 18% 58%, rgba(255,255,255,0.18) 0, rgba(255,255,255,0) 12%);
  }
  .book-cover__badge,
  .book-cover__author {
    position: absolute;
    left: 0;
    right: 0;
    text-align: center;
    font-family: "Montserrat", sans-serif;
    color: var(--ink);
  }
  .book-cover__badge {
    top: 52px;
    font-size: 17px;
    font-weight: 600;
    letter-spacing: 0.24em;
  }
  .book-cover__author {
    top: 110px;
    font-size: 27px;
    font-weight: 700;
    letter-spacing: 0.32em;
  }
  .book-cover__title {
    position: absolute;
    left: 44px;
    top: 290px;
    width: 420px;
    height: 90px;
  }
  .book-cover__title text {
    font-family: "Anton", sans-serif;
    font-size: 86px;
  }
  .book-cover__subtitle {
    position: absolute;
    left: 0;
    right: 0;
    top: 470px;
    text-align: center;
    font-family: "Source Sans 3", sans-serif;
    font-weight: 700;
    font-size: 36px;
    line-height: 1.45;
    color: var(--ink);
  }
</style>
</head>
<body>
<main class="canvas">
  <section class="book-cover" aria-label="Book cover: Unwavering by Carla Jean Morrow">
    <div class="book-cover__shimmer"></div>
    <p class="book-cover__badge">DAILY MERIDIAN BEST SELLER</p>
    <p class="book-cover__author">CARLA JEAN MORROW</p>
    <svg class="book-cover__title" viewBox="0 0 420 90" role="heading" aria-level="1" aria-label="UNWAVERING">
      <text x="210" y="82" text-anchor="middle" textLength="410" lengthAdjust="spacingAndGlyphs"
            fill="var(--ink)" stroke="var(--ink)" stroke-width="7" stroke-linejoin="round">UNWAVERING</text>
      <text x="210" y="82" text-anchor="middle" textLength="410" lengthAdjust="spacingAndGlyphs"
            fill="var(--ink)" stroke="var(--glow)" stroke-width="2.2" stroke-linejoin="round">UNWAVERING</text>
    </svg>
    <p class="book-cover__subtitle">Ways to Kindle the<br>Spark of Resolve</p>
  </section>
</main>
</body>
</html>
```